VELVET ORBITS - BOOK COVER

I have written a book called VELVET ORBIT - HOW TO CLIMB PAST EVERY LIMIT TO THE TOP RUNG. I need a front cover design for the book. The book cover needs to be intriguing for someone to pick it up and read the first couple of pages. I want people to think about ACHIEVING SUCCESS when they read this book.
PLEASE LOOK AT THE ATTACHMENT. THANKS!

Target Market(s)

males, entrepreneurs, small business owners, salespeople, corporate executives

Industry/Entity Type

Business

Logo Text

VELVET ORBITS

Logo styles of interest
Emblem Logo
Abstract Logo
Font styles to use
Serif
Sans Serif

Colors
ec1f27
000000
959595
ffffff

Requirements
Must have
• It has to have a "hurricane" feel to it with hurricane colors.
Nice to have
• I open to your ideas
Should not have
• no other colors except red, black, gray, white.

```html
<!DOCTYPE html>
<html lang="en">
<head>
<meta charset="utf-8">
<title>Velvet Orbits – Book Cover</title>
<link rel="stylesheet" href="https://fonts.googleapis.com/css2?family=Arimo:wght@400;700&display=swap">
<style>
  :root {
    --page: #ffffff;
    --cover: #000000;
    --red: #ec1f27;
    --white: #ffffff;
    --grey: #959595;
  }
  * { margin: 0; padding: 0; box-sizing: border-box; }
  html, body {
    width: 1200px;
    height: 849px;
    overflow: hidden;
    background: var(--page);
  }
  .canvas {
    position: relative;
    width: 1200px;
    height: 849px;
    background: var(--page);
    font-family: "Arimo", Arial, sans-serif;
  }
  .cover {
    position: absolute;
    left: 394px;
    top: 134px;
    width: 401px;
    height: 572px;
    background: var(--cover);
    color: var(--white);
  }
  .title {
    position: absolute;
    top: 46px;
    left: 0;
    width: 100%;
    text-align: center;
    font-weight: 400;
    line-height: 1;
  }
  .title__top {
    display: block;
    font-size: 44px;
    color: var(--red);
    letter-spacing: 0.5px;
  }
  .title__bottom {
    display: block;
    margin-top: 2px;
    font-size: 44px;
    color: var(--white);
  }
  .title__tm {
    font-size: 13px;
    vertical-align: top;
    position: relative;
    top: 4px;
  }
  .brand-mark {
    position: absolute;
    top: 250px;
    left: 0;
    width: 100%;
    display: flex;
    justify-content: center;
    align-items: center;
    gap: 10px;
  }
  .brand-mark__dot {
    width: 18px;
    height: 18px;
    border-radius: 50%;
    background: var(--red);
  }
  .brand-mark__name {
    font-size: 22px;
    font-weight: 700;
    color: var(--red);
    letter-spacing: 1px;
  }
  .subtitle {
    position: absolute;
    top: 396px;
    left: 0;
    width: 100%;
    display: flex;
    justify-content: center;
    align-items: stretch;
  }
  .subtitle__lead {
    text-align: right;
    padding-right: 8px;
    display: flex;
    flex-direction: column;
    justify-content: center;
    line-height: 1.05;
  }
  .subtitle__small {
    font-size: 9px;
    font-weight: 700;
    color: var(--white);
  }
  .subtitle__accent {
    font-size: 17px;
    font-weight: 400;
    color: var(--red);
  }
  .subtitle__rule {
    width: 1px;
    background: var(--white);
  }
  .subtitle__level {
    padding-left: 8px;
    display: flex;
    flex-direction: column;
    align-items: center;
    line-height: 1.05;
  }
  .subtitle__level-top {
    font-size: 10px;
    color: var(--white);
  }
  .subtitle__triangle {
    display: block;
    margin: 3px 0 2px;
  }
  .subtitle__level-bottom {
    font-size: 13px;
    font-weight: 700;
    color: var(--red);
  }
  .author {
    position: absolute;
    top: 508px;
    left: 0;
    width: 100%;
    text-align: center;
    font-size: 10px;
    font-weight: 700;
    letter-spacing: 3px;
    color: var(--white);
  }
</style>
</head>
<body>
<main class="canvas">
  <section class="cover" aria-label="Book cover: Velvet Orbit">
    <h1 class="title">
      <span class="title__top">VELVET</span>
      <span class="title__bottom">ORBITS<span class="title__tm">™</span></span>
    </h1>

    <div class="brand-mark">
      <span class="brand-mark__dot"></span>
      <span class="brand-mark__name">VELVET ORBITS</span>
    </div>

    <div class="subtitle">
      <div class="subtitle__lead">
        <span class="subtitle__small">HOW TO CLIMB</span>
        <span class="subtitle__accent">PAST EVERY</span>
        <span class="subtitle__small">LIMIT TO</span>
      </div>
      <div class="subtitle__rule"></div>
      <div class="subtitle__level">
        <span class="subtitle__level-top">THE TOP</span>
        <svg class="subtitle__triangle" width="24" height="20" viewBox="0 0 24 20" aria-hidden="true">
          <path d="M12 1 L23 19 L1 19 Z" fill="#ec1f27" stroke="#ec1f27" stroke-linejoin="round" stroke-width="2"/>
        </svg>
        <span class="subtitle__level-bottom">RUNG</span>
      </div>
    </div>

    <p class="author">CAL MERRIDEW</p>
  </section>
</main>
</body>
</html>
```